Coastwell Keys Agency Guarantee

We need a flyer to promote a Sydney based property management agency.
We specialise in Property Management on the Northern Beaches of Sydney. A small boutique agency that prides itself on high quality customer service and the lowest fees.
We would like this flyer to promote our listed features in the document provided and focus on our money back guarantee.
The flyer must:
- be designed to match our website www.coastwellkeysagency.com.au
- Contain our logo and contact details
- Use the attached photoshop template for bleed, sizing and fold lines
- final files must include a print ready PDF and fully editable PSD (photoshop) file with included fonts.
Attached are the following files:
Contact details are:
Name: Tom Farrow
Tel: 0491 527 068
email: tom@coastwellkeysagency.com.au
Office: Level 2, 17 Tennerby Rd, Marlowe Bay NSW 2718
Web: www.coastwellkeysagency.com.au
Target Market(s)
35-75yo Male and Females that own investment properties on Sydney's Norther Beaches
Industry/Entity Type
Real Estate
Requirements
Must have
- The flyer must:
- - Be double sided and colour
- - be designed to match our website www.coastwellkeysagency.com.au
- - Contain our logo and contact details
- - Use the attached photoshop template for bleed, sizing and fold lines
- - final files must include a print ready PDF and fully editable PSD (photoshop) file with included fonts.
Nice to have
- A Money back guarantee "stamp"

```html
<!DOCTYPE html>
<html lang="en">
<head>
<meta charset="utf-8">
<title>Coastwell Keys Agency – Tri-fold Brochure</title>
<link href="https://fonts.googleapis.com/css2?family=Open+Sans:wght@400;600;700;800&family=Roboto+Condensed:wght@700&display=swap" rel="stylesheet">
<style>
:root{
  --teal:#1e9aa8;
  --teal-dark:#137784;
  --teal-light:#7fd0d8;
  --ink:#1c2a33;
  --text:#3c4a52;
  --paper:#f2f5f6;
  --paper-shade:#e3e9eb;
  --stage:#ffffff;
}
*{box-sizing:border-box;margin:0;padding:0}
html,body{width:1200px;height:482px;overflow:hidden;background:var(--stage)}
body{position:relative;font-family:"Open Sans",sans-serif;color:var(--text)}
.spread{position:absolute;top:36px;width:560px;height:410px;display:flex;box-shadow:0 2px 8px rgba(0,0,0,.18);overflow:hidden;background:var(--paper)}
.spread--inside{left:40px}
.spread--outside{left:620px}
.panel{position:relative;width:186.67px;height:100%;overflow:hidden;border-right:1px solid var(--paper-shade)}
.panel:last-child{border-right:0}
.panel__body{position:absolute;left:9px;right:9px}
.heading{display:inline-block;font-weight:800;font-size:7.4px;text-transform:uppercase;color:var(--ink);margin:6px 0 3px;letter-spacing:.1px}
.heading b{background:var(--teal);color:#fff;padding:1px 3px;font-weight:800}
.heading--bar{display:block;background:var(--ink);color:#fff;padding:2px 4px}
.copy{font-size:4.9px;line-height:1.42;margin-bottom:3px}
.note{font-size:4.4px;font-style:italic;line-height:1.4;margin-bottom:3px}
.bullets{list-style:none}
.bullets li{position:relative;padding-left:9px;font-size:4.9px;line-height:1.42;margin-bottom:4px}
.bullets svg{position:absolute;left:0;top:1px}
.photo{position:absolute}
.photo--harbour{left:0;top:0;width:187px;height:150px;background:linear-gradient(170deg,#5a9fd6 0%,#a9cfe9 40%,#6c8a9a 70%,#3d5563 100%);clip-path:polygon(0 0,100% 0,100% 100%,0 78%)}
.photo--house{right:0;bottom:0;width:187px;height:170px;background:linear-gradient(160deg,#6eb1e0 0%,#cfe1ea 35%,#7f8f86 65%,#3e5a3c 100%);clip-path:polygon(22% 0,100% 0,100% 100%,0 100%,0 30%)}
.photo--terrace{left:0;top:0;width:187px;height:215px;background:linear-gradient(165deg,#5e9fd0 0%,#c9dde8 40%,#7c8a8a 70%,#3f5542 100%);clip-path:polygon(0 0,100% 0,100% 100%,30% 80%,0 62%)}
.photo--cover{left:0;top:44px;width:187px;height:190px;background:linear-gradient(170deg,#6ab0e2 0%,#d6e6ee 38%,#9aa6a4 62%,#4d6048 100%);clip-path:polygon(0 0,100% 0,100% 78%,40% 100%,0 55%)}
.deco{position:absolute;inset:0;pointer-events:none}
.brand{position:absolute;right:10px;top:14px;font-weight:700;font-size:10px;color:#fff;text-transform:uppercase;letter-spacing:.3px;display:flex;align-items:center;gap:4px;z-index:2}
.brand__mark{width:6px;height:6px;background:var(--teal-light)}
.cover-title{position:absolute;right:10px;top:262px;text-align:right;font-family:"Roboto Condensed",sans-serif;font-weight:700;text-transform:uppercase;color:var(--ink);line-height:1}
.cover-title span{display:block;font-size:19px}
.cover-title .cover-title__accent{display:inline-block;margin-top:2px;background:var(--teal);color:#fff;font-size:15px;padding:2px 5px}
.services{position:absolute;right:0;top:346px;display:flex;flex-direction:column;align-items:flex-end;gap:2px}
.services span{background:var(--ink);color:#fff;font-weight:700;font-size:6px;text-transform:uppercase;padding:3px 6px}
.contact{position:absolute;left:0;right:0;top:292px;text-align:center}
.contact__name{display:inline-block;border:1.5px solid var(--teal);color:var(--teal);font-weight:800;font-size:9.5px;text-transform:uppercase;padding:2px 14px;margin-bottom:6px;background:#fff}
.contact p{font-size:5.4px;line-height:1.6;color:var(--ink)}
</style>
</head>
<body>

<section class="spread spread--inside">
  <div class="panel">
    <div class="photo photo--harbour" role="img" aria-label="Photo of a harbourside promenade with apartments on a sunny day"></div>
    <svg class="deco" width="187" height="410" viewBox="0 0 187 410"><polygon points="0,117 187,150 187,156 0,126" fill="#1e9aa8"/></svg>
    <div class="panel__body" style="top:158px">
      <h2 class="heading"><b>Strict Screening</b> Process</h2>
      <p class="copy">All tenancy applications go through a rigorous screening process to ensure we only put forward the best tenants for the landlord's final selection.</p>
      <p class="copy">The screening process includes the most up-to-date tenancy database blacklists, financial background checks and employment checks just to list a few.</p>
      <h2 class="heading"><b>Quality Tenant Database</b> and Corporate Re-locators</h2>
      <p class="copy">As we do many openings for properties we get to meet a lot of quality tenants. We take pride in building our database with quality tenants and the type of property they are interested in. It's not uncommon for us to have a screened quality tenant ready to move straight into your property. Ensuring the minimization of unattended periods.</p>
      <p class="copy">We also work closely with corporate re-locators, getting corporate professionals arriving from interstate or internationally into your property.</p>
    </div>
  </div>
  <div class="panel">
    <div class="panel__body" style="top:4px">
      <h2 class="heading"><b>Quick to Act and Tenant</b> a Property</h2>
      <p class="copy">As we do many openings for properties we get to meet a lot of quality tenants. We take pride in building our database with quality tenants and the type of property they are interested in. It's not uncommon for us to have a screened quality tenant ready to move straight into your property. Ensuring the minimization of unattended periods.</p>
      <p class="copy">We also work closely with corporate re-locators, getting corporate professionals arriving from interstate or internationally into your property.</p>
      <h2 class="heading"><b>6 Monthly Property</b> Reports</h2>
      <p class="copy">We go above and beyond when it comes to reports on your property's performance.</p>
      <p class="copy">In conjunction with routine inspections every 6 months, we also produce property valuation reports and in-depth Comparative Market Analysis for your property. These reports detail similar properties within close proximity to yours, how they have performed on the market in both sales and rentals. Included in the report are details on the local market in general and how your property has performed, compares and is currently valued at.</p>
      <h2 class="heading"><b>Landlord</b> Portal</h2>
      <p class="copy">At Coastwell Keys Agency we have heavily invested into our cloud-based property management software. With our Landlord Portal, you can log in to download financial reports, live job or maintenance updates as well as detailed photos and videos of your latest inspection. It allows you to stay up-to-date with your property and make sure everything is running the way it should be.</p>
      <h2 class="heading"><b>Maintenance/Renovation</b> Plan</h2>
      <p class="copy">Another service we offer is maintenance and renovation plans. A common misconception with an investment property is that you want to spend as little as possible on the property, to maximize the yield.</p>
      <p class="copy">While our job is to ensure the best financial performance of your property there are two very strong reasons to put together a maintenance/renovation plan for your property.</p>
      <ul class="bullets">
        <li><svg width="6" height="6" viewBox="0 0 6 6"><path d="M1 0l4 3-4 3z" fill="#1e9aa8"/></svg>Building Equity: Renovations add value to your property, and it might be worth spending $20k on a renovation to increase your properties value up to $60k or more potentially giving you the equity needed to invest in your next property.</li>
        <li><svg width="6" height="6" viewBox="0 0 6 6"><path d="M1 0l4 3-4 3z" fill="#1e9aa8"/></svg>Ensuring that you aren't ignoring small maintenance issues that could become expensive big problems in the future.</li>
      </ul>
    </div>
  </div>
  <div class="panel">
    <div class="panel__body" style="top:4px">
      <h2 class="heading"><b>Retaining Great</b> Tenants</h2>
      <p class="copy">Here at Coastwell Keys Agency we understand the value of quality tenants. They ensure your investment property is well looked after, rent is paid on time and make our jobs here much easier.</p>
      <p class="copy">We like to let quality tenants know that we appreciate them. From time to time we send out small rewards and gifts to thank them for being great, paying on time and looking after your property.</p>
      <p class="copy">Right now we are sending out a little Christmas gift and card to all our tenants. This is not something we charge landlords for, we just want to hold on to quality tenants and show them our appreciation.</p>
      <h2 class="heading"><b>Our Broad</b> Team</h2>
      <p class="copy">Not only do we have a friendly, professional and efficient property management team, we also work closely with associated builders, accountants and mortgage brokers. So you have access to experienced professionals in all facets of property investment.</p>
      <p class="copy">We work for you and its in our best interest that you get the best advice and service possible to get the most out of your investment.</p>
    </div>
    <div class="photo photo--house" role="img" aria-label="Photo of a modern two-storey coastal house with a lawn"></div>
    <svg class="deco" width="187" height="410" viewBox="0 0 187 410"><polygon points="0,291 41,240 45,240 0,297" fill="#1e9aa8"/></svg>
  </div>
</section>

<section class="spread spread--outside">
  <div class="panel">
    <div class="panel__body" style="top:4px">
      <h2 class="heading heading--bar">What separates Coastwell Keys Agency</h2>
      <p class="copy">Coastwell Keys Agency is a boutique agency that specialises in Property Management.</p>
      <p class="copy">We differ from your typical agency because our primary business is property management. You will have a senior property manager that is solely focused on maximising your investments potential. As property investors ourselves we understand the frustrations you have with a typical agency, and we promise to offer you the service, care and professionalism beyond what you expect. Guaranteed!</p>
      <h2 class="heading heading--bar">Our Guarantee</h2>
      <p class="copy">At Coastwell Keys Agency we are the Risk Reduction Specialists! Our team will work with you to ensure you're receiving the highest possible return on your investment property. The entire department are heavily focused on maximising your income and optimising capital growth on your investment property.</p>
      <p class="copy">We understand when you are selecting a new managing agent it can be a very stressful process for many landlords as you don't know if they are going to deliver on their promises. At Coastwell Keys Agency we understand promises can be easily broken and the good news is we GUARANTEE our service.</p>
      <p class="copy">If during the first 3 months you are not satisfied with our level of service we promise to you. We are prepared to refund the first 3 months and will give 100% money back on your management fees.</p>
      <p class="note">* Only applies to management fees. Coastwell Keys Agency must be notified in writing within the 3 month service guarantee period.</p>
      <h2 class="heading heading--bar">Keeping it Simple</h2>
      <p class="copy">At the core of our business, we want to keep things simple for you. We understand you have other important things to worry about, so leave your property in the hands of our professional staff, and let them make life easier for you.</p>
      <h2 class="heading heading--bar">Senior Property Manager</h2>
      <p class="copy">The key to any good relationship is people. We have great people that are given the tools needed to manage your property to its full potential.</p>
      <p class="copy">Unlike most agencies our focus is property management, not sales. This means we appoint a senior property manager to ensure smooth professional management of your investment.</p>
      <p class="copy">Our property managers are not overloaded with hundreds of properties to manage individually. We want to be able to give you and your property the attention they deserve.</p>
    </div>
  </div>
  <div class="panel">
    <div class="photo photo--terrace" role="img" aria-label="Photo of a modern apartment building with balconies and gardens"></div>
    <svg class="deco" width="187" height="410" viewBox="0 0 187 410">
      <polygon points="0,134 56,172 60,168 0,127" fill="#1e9aa8"/>
      <polygon points="56,172 187,215 187,222 52,176" fill="#137784"/>
    </svg>
    <div class="contact">
      <div class="contact__name">Tom Farrow</div>
      <p>0491 527 068</p>
      <p>tom@coastwellkeysagency.com.au</p>
      <p>www.coastwellkeysagency.com.au</p>
      <p>Level 2, 17 Tennerby Rd, Marlowe Bay NSW 2718</p>
    </div>
  </div>
  <div class="panel">
    <svg class="deco" width="187" height="410" viewBox="0 0 187 410">
      <polygon points="0,0 187,0 187,60 0,40" fill="#1e9aa8"/>
    </svg>
    <div class="brand"><span class="brand__mark"></span>Coastwell Keys</div>
    <div class="photo photo--cover" role="img" aria-label="Photo of a smiling property manager standing in front of a modern coastal home"></div>
    <svg class="deco" width="187" height="410" viewBox="0 0 187 410">
      <polygon points="0,148 75,234 187,192 187,200 75,244 0,158" fill="#1e9aa8"/>
    </svg>
    <h1 class="cover-title"><span>Property</span><span>Management</span><span class="cover-title__accent">Done Right!</span></h1>
    <div class="services">
      <span>Rental Appraisal</span>
      <span>Referral Program</span>
      <span>Property Management Transfer</span>
    </div>
  </div>
</section>

</body>
</html>
```